Kolmister Technologies LOGO, Business Card, and Stationary Project
Kolmister Technologies
Kolmister Technologies LOGO, Business Card, and Stationary Project - Consulting
Creative Brief
Modern
Tobias Whelkin
President / CEO
417 North Pellham Road # Davidsonville, Maryland 20964
twhelkin@kolmister-example.com
www.kolmister-example.com
Note to Winner: The final files created for this project will need to be sent to the Project Holder to allow for updates to address or adding new employees to business cards or stationary. Ensure that final copies are sent unlayerd in Adobe PSD format.
We Build the Technology Future Today

```html
<!DOCTYPE html>
<html lang="en">
<head>
<meta charset="utf-8">
<title>Kolmister Technologies Stationery</title>
<link href="https://fonts.googleapis.com/css2?family=Roboto:wght@400;700&display=swap" rel="stylesheet">
<style>
:root{
  --bg-dark:#1c1c1c;
  --bg-mid:#3a3a3a;
  --paper:#ffffff;
  --paper-shade:#e9e9e9;
  --ink:#333333;
  --ink-soft:#8a8a8a;
  --brand-red:#c8102e;
  --brand-red-dark:#7a0a1a;
  --card-dark:#151515;
}
*{margin:0;padding:0;box-sizing:border-box}
html,body{width:1200px;height:290px;overflow:hidden}
body{font-family:'Roboto',Arial,sans-serif;background:radial-gradient(ellipse at 50% 40%,var(--bg-mid),var(--bg-dark) 80%);position:relative}
.piece{position:absolute;overflow:hidden;box-shadow:0 3px 8px rgba(0,0,0,.6)}
.wordmark{display:flex;align-items:center;gap:3px;color:var(--brand-red);font-weight:700;white-space:nowrap}
.wordmark .dot{width:.9em;height:.9em;border-radius:50%;background:var(--brand-red)}
.wordmark.light{color:var(--paper)}
.wordmark.light .dot{background:var(--brand-red)}
.tiny{font-size:4px;line-height:6px;color:var(--ink-soft)}
.card{width:101px;height:58px}
.card.light{background:var(--paper)}
.card.dark{background:var(--card-dark)}
.card .wordmark{position:absolute;font-size:9px}
.card .band{position:absolute;right:0;top:0;bottom:0;width:22px;background:linear-gradient(var(--brand-red),var(--brand-red-dark))}
.card .info{position:absolute;left:8px;bottom:6px}
.card.dark .tiny{color:#bbbbbb}
.swoosh{position:absolute;left:0;width:100%}
.letterhead{width:140px;height:264px;top:12px;background:var(--paper)}
.letterhead .wordmark{position:absolute;left:10px;top:12px;font-size:8px}
.letterhead .footer{position:absolute;left:10px;bottom:12px}
.envelope{background:var(--paper)}
.envelope .wordmark{position:absolute;left:8px;top:6px;font-size:7px}
.folder{left:852px;top:12px;width:324px;height:264px;display:flex}
.folder .cover{width:50%;background:linear-gradient(135deg,#2b2b2b,#0d0d0d);position:relative}
.folder .inside{width:50%;background:linear-gradient(135deg,#202020,#090909);position:relative}
.folder .cover .wordmark{position:absolute;left:22px;top:70px;font-size:14px}
.folder .tag{position:absolute;left:22px;top:92px;font-size:5px;color:#aaaaaa;letter-spacing:.5px}
</style>
</head>
<body>

<!-- Business cards -->
<div class="piece card light" style="left:72px;top:48px">
  <div class="wordmark" style="left:8px;top:8px"><span class="dot"></span>Kolmister</div>
  <div class="band"></div>
  <div class="info tiny">Tobias Whelkin<br>President / CEO<br>Tel 410.555.0148</div>
</div>
<div class="piece card dark" style="left:187px;top:48px">
  <div class="info tiny" style="top:10px;bottom:auto">417 North Pellham Road<br>Davidsonville, Maryland 20964<br>twhelkin@kolmister-example.com<br>www.kolmister-example.com</div>
  <svg class="swoosh" style="bottom:0" viewBox="0 0 101 14" height="14" preserveAspectRatio="none"><path d="M0 14 Q50 0 101 6 L101 14Z" fill="var(--brand-red)"/></svg>
</div>
<div class="piece card light" style="left:72px;top:125px">
  <div class="wordmark" style="left:18px;top:22px"><span class="dot"></span>Kolmister</div>
</div>
<div class="piece card dark" style="left:187px;top:125px">
  <div class="wordmark light" style="left:18px;top:22px"><span class="dot"></span>Kolmister</div>
</div>
<div class="piece card light" style="left:72px;top:204px">
  <div class="wordmark" style="left:8px;top:8px"><span class="dot"></span>Kolmister</div>
  <div class="info tiny">Technologies</div>
</div>
<div class="piece card dark" style="left:187px;top:204px">
  <div class="info tiny" style="top:10px;bottom:auto">Tobias Whelkin<br>President / CEO<br>Tel 410.555.0148</div>
  <svg class="swoosh" style="bottom:0" viewBox="0 0 101 14" height="14" preserveAspectRatio="none"><path d="M0 14 Q50 0 101 6 L101 14Z" fill="var(--brand-red)"/></svg>
</div>

<!-- Letterheads -->
<div class="piece letterhead" style="left:305px">
  <svg class="swoosh" style="top:0" viewBox="0 0 140 40" height="40" preserveAspectRatio="none"><path d="M0 0 H140 V10 Q70 32 0 18Z" fill="var(--paper-shade)"/><path d="M0 18 Q70 32 140 10 V13 Q70 36 0 21Z" fill="var(--brand-red)"/></svg>
  <div class="wordmark"><span class="dot"></span>Kolmister</div>
  <svg class="swoosh" style="bottom:0" viewBox="0 0 140 24" height="24" preserveAspectRatio="none"><path d="M0 24 Q70 0 140 14 V24Z" fill="var(--brand-red)"/></svg>
  <div class="footer tiny">417 North Pellham Road · Davidsonville, Maryland 20964</div>
</div>
<div class="piece letterhead" style="left:454px">
  <svg class="swoosh" style="top:0" viewBox="0 0 140 40" height="40" preserveAspectRatio="none"><path d="M0 0 H140 V10 Q70 32 0 18Z" fill="var(--paper-shade)"/><path d="M0 18 Q70 32 140 10 V13 Q70 36 0 21Z" fill="var(--brand-red)"/></svg>
  <div class="wordmark"><span class="dot"></span>Kolmister</div>
  <div class="footer tiny">www.kolmister-example.com</div>
</div>

<!-- Envelopes -->
<div class="piece envelope" style="left:605px;top:18px;width:228px;height:78px">
  <svg viewBox="0 0 228 78" width="228" height="78" style="position:absolute;inset:0"><path d="M0 0 L114 40 L228 0" fill="none" stroke="var(--paper-shade)" stroke-width="2"/><path d="M0 78 Q114 50 228 66 V78Z" fill="var(--brand-red)"/></svg>
</div>
<div class="piece envelope" style="left:615px;top:108px;width:210px;height:58px;background:linear-gradient(#d6d6d6,#9a9a9a)">
  <svg viewBox="0 0 210 58" width="210" height="58" style="position:absolute;inset:0"><path d="M0 0 L105 34 L210 0Z" fill="var(--paper)"/></svg>
</div>
<div class="piece envelope" style="left:605px;top:176px;width:228px;height:40px">
  <div class="wordmark"><span class="dot"></span>Kolmister</div>
  <svg class="swoosh" style="bottom:0" viewBox="0 0 228 10" height="10" preserveAspectRatio="none"><path d="M0 10 Q114 0 228 4 V10Z" fill="var(--brand-red)"/></svg>
</div>
<div class="piece envelope" style="left:640px;top:228px;width:160px;height:48px">
  <div class="wordmark"><span class="dot"></span>Kolmister</div>
  <div class="tiny" style="position:absolute;left:8px;top:18px">417 North Pellham Road</div>
  <svg class="swoosh" style="bottom:0" viewBox="0 0 160 10" height="10" preserveAspectRatio="none"><path d="M0 10 Q80 0 160 4 V10Z" fill="var(--brand-red)"/></svg>
</div>

<!-- Presentation folder -->
<div class="piece folder">
  <div class="cover">
    <div class="wordmark"><span class="dot"></span>Kolmister</div>
    <div class="tag">We Build the Technology Future Today</div>
    <svg class="swoosh" style="bottom:0" viewBox="0 0 162 40" height="40" preserveAspectRatio="none"><path d="M0 40 Q80 10 162 22 V40Z" fill="var(--brand-red)"/></svg>
  </div>
  <div class="inside">
    <svg class="swoosh" style="bottom:0" viewBox="0 0 162 90" height="90" preserveAspectRatio="none"><path d="M0 30 Q60 0 162 20 V90 H0Z" fill="var(--brand-red-dark)"/><path d="M0 40 Q60 12 162 30 V90 H0Z" fill="var(--brand-red)"/></svg>
  </div>
</div>

</body>
</html>
```